Ridgeline Orchards Organic Cherry POS card 7x11

We are wanting to create a one-sided 7 x 11 organic cherry card that is eye catching and informative.This should be clear and easy to read and not cluttered. We use these cards as a display in grocery stores, demo stands, and other events to market Organic Ridgeline Sweet Orchards. We have a few facts that we would like displayed on the card (see attachment).

Target Market(s)

Consumers

Industry/Entity Type

Agriculture

Requirements
Must have
• Natural color palettes
• Easy to read
• Ridgeline Orchards
Nice to have
• Unique, realistic cherry design

```html
<!DOCTYPE html>
<html lang="en">
<head>
<meta charset="utf-8">
<title>Ridgeline Orchards – Organic Cherry Card</title>
<link rel="stylesheet" href="https://fonts.googleapis.com/css2?family=Arimo:wght@400;700&family=Libre+Baskerville:ital,wght@1,700&display=swap">
<style>
  :root {
    --green-dark: #1f5a2a;
    --green: #2f7d32;
    --cherry-deep: #5a0610;
    --cherry: #9e1020;
    --cherry-light: #c9303b;
    --badge: #8c1420;
    --red-heading: #c8202a;
    --ink: #333333;
    --white: #ffffff;
  }
  * { box-sizing: border-box; margin: 0; padding: 0; }
  html, body { width: 764px; height: 1200px; overflow: hidden; background: var(--white); }
  .card {
    position: relative;
    width: 764px;
    height: 1200px;
    background: var(--white);
    font-family: "Arimo", Arial, sans-serif;
    color: var(--ink);
    overflow: hidden;
  }
  .brand {
    position: absolute;
    left: 34px;
    top: 30px;
    display: flex;
    align-items: center;
    gap: 14px;
    z-index: 2;
  }
  .brand-dot {
    width: 44px; height: 44px;
    border-radius: 50%;
    background: var(--cherry);
  }
  .brand-name {
    font-weight: 700;
    font-size: 34px;
    color: var(--green-dark);
  }
  .feature { position: absolute; left: 0; top: 0; width: 764px; height: 930px; }
  .ring-text {
    font-family: "Arimo", Arial, sans-serif;
    font-size: 24px;
    fill: var(--white);
  }
  .headline {
    position: absolute;
    left: 200px;
    top: 240px;
    width: 540px;
    font-family: "Libre Baskerville", Georgia, serif;
    font-style: italic;
    font-weight: 700;
    font-size: 56px;
    line-height: 76px;
    color: var(--white);
    text-shadow: 3px 3px 6px rgba(0,0,0,0.6);
  }
  .headline span { display: block; }
  .headline .l1 { padding-left: 40px; }
  .headline .l2 { padding-left: 20px; }
  .headline .l5 { padding-left: 140px; }
  .benefits { position: absolute; left: 34px; top: 905px; }
  .benefits h2 {
    font-size: 30px;
    line-height: 36px;
    font-weight: 700;
    color: var(--red-heading);
    margin-bottom: 6px;
  }
  .benefits ul { list-style: none; }
  .benefits li {
    font-size: 22px;
    line-height: 30px;
    display: flex;
    align-items: center;
    gap: 10px;
  }
  .benefits li::before {
    content: "";
    width: 11px; height: 11px;
    border-radius: 50%;
    background: var(--green);
  }
  .badge {
    position: absolute;
    left: 584px; top: 944px;
    width: 156px; height: 156px;
    border-radius: 50%;
    background: var(--badge);
    border: 4px solid var(--white);
    box-shadow: 0 0 0 3px var(--badge);
    color: var(--white);
    display: flex; flex-direction: column; align-items: center; justify-content: center;
    font-weight: 700;
    text-align: center;
  }
  .badge .fat { font-size: 50px; line-height: 50px; }
  .badge .free { font-size: 30px; line-height: 32px; }
  .contacts {
    position: absolute; left: 34px; top: 1112px;
    display: flex; font-size: 16px; line-height: 24px; color: var(--ink);
  }
  .contacts span { padding: 0 22px; border-left: 2px solid var(--green); }
  .contacts span:first-child { padding-left: 0; border-left: 0; }
  .footer-bar {
    position: absolute; left: 0; bottom: 0;
    width: 764px; height: 48px;
    background: var(--green-dark);
    color: var(--white);
    display: flex; align-items: center; justify-content: center;
    font-size: 20px; font-weight: 700; letter-spacing: 4px;
  }
</style>
</head>
<body>
<div class="card">
  <div class="brand">
    <div class="brand-dot"></div>
    <div class="brand-name">Ridgeline Orchards</div>
  </div>

  <svg class="feature" viewBox="0 0 764 930" xmlns="http://www.w3.org/2000/svg">
    <defs>
      <radialGradient id="cherry-fill" cx="55%" cy="45%" r="65%">
        <stop offset="0" stop-color="#c9303b"/>
        <stop offset="0.5" stop-color="#9e1020"/>
        <stop offset="1" stop-color="#5a0610"/>
      </radialGradient>
      <path id="ring-path" d="M 423.2 104.1 A 400 400 0 1 0 729 842.5"/>
    </defs>
    <circle cx="560" cy="480" r="378" fill="url(#cherry-fill)" role="img" aria-label="Close-up photo of ripe red cherries"/>
    <circle cx="560" cy="480" r="400" fill="none" stroke="#1f5a2a" stroke-width="44"/>
    <text class="ring-text" dy="9">
      <textPath href="#ring-path" textLength="1250" lengthAdjust="spacing">WASHINGTON STATE IS THE NATION’S LARGEST PRODUCER OF ORGANIC CHERRIES.</textPath>
    </text>
  </svg>

  <p class="headline">
    <span class="l1">Organic</span>
    <span class="l2">Northwest</span>
    <span>cherries make up</span>
    <span>1/3 of the</span>
    <span class="l5">nation’s</span>
    <span class="l5">production.</span>
  </p>

  <section class="benefits">
    <h2>HEALTH BENEFITS:</h2>
    <ul>
      <li>Source of Vitamin C</li>
      <li>A Natural Anti-Inflammatory</li>
      <li>Source of Potassium</li>
      <li>Source of Melatonin</li>
    </ul>
  </section>

  <div class="badge"><span class="fat">FAT</span><span class="free">Free</span></div>

  <div class="contacts">
    <span>0000 111 222</span>
    <span>Your Address Here</span>
    <span>Your@emailhere.com</span>
  </div>

  <div class="footer-bar">www.ridgelineorchards.com</div>
</div>
</body>
</html>
```